Osteopath Advert Flyer for 20% discount

Osteopathic treatment services (much like the flyer design I found on google which brought me to your website - "Bodywise Restful Healing"
I very much like the left side of that screenshot with the graphic design body rather than a real person.
If double sided, here are further details for what it is I do (this is optional if it is double sided). Ideally one side eye catching and the other with more information.
____________________________
Osteopathy can offer great results for those seeking immediate care with painful conditions and also for those wishing to invest in long-term health solutions. Treatments are tailored to the individual’s need, regardless of age or condition, my goal is to provide the best medical care whether it be treatment or more appropriate referral.

Osteopathy focuses on health promotion and disease prevention in order to help each person achieve a high level of wellness.

Osteopathy uses conventional medical assessment and techniques when gathering detail during diagnostic procedures. However, the real strength of osteopathy lies within the unique approach to which a patient and the condition are assessed and treated. Each patient is assessed from both a mechanical and functional viewpoint and treatment is based on these findings and patient requirements. Manual treatment methods are applied to suit the needs of the individual patient.

The overall goal is to achieve wellness by restoring balance and flexibility to the whole body.
_____________________________
I live in a small Island called Jersey and word-of-mouth is everything here. Therefore, I'd like a flyer that clearly indicates I treat people and aim to help people out of pain and injury but also give a very relaxing and enjoyable experience. So, not too clinical but also not to imaginary/idealistic massage room spa treatment.

Osteopathy is more or less in between a physio and a chiropractor (with regards to design style of this flyer). Of course it is somewhat very different to those professions, however, for this purpose the overall aim/style would be similar.

Please note: I do not particularly desire being on the flyer myself, however, it could be quite useful so I am happy for you to decide whether it may be of benefit.The aim is to attract the eye of the people walking past the flyer and to look professional but also interesting as many people will not have seen an osteopath before.

Thank you!

Target Market(s)

All humans above ages for 10

Industry/Entity Type

Healthcare

Font styles to use
Serif
Sans Serif

Colors
3377b5
33a6d7
ffffff
34a7d7
3277b5
85acd3
85cae6

Requirements
Must have
• 07461 352 417
contact@belvantoske.co.uk
www.belvantoske.co.uk

Copper Mead Clinic
La Rue Des Pins
St Lawrence
Jersey
JE2 4QW

20% off with this flyer (*for initial consultation only*)
Nice to have
• Initial Consultation £55 for 45 minutes
Follow-Up Treatment £50 for 30 minutes

Treatment areas (much like in the flyers I attached as screenshots from google)
Headaches
Neck pain
Shoulder pain
Elbow and hand pain
Back pain
Hip pain
Knee pain
Ankle and foot pain
Arthritic pains
Chronic pain
Should not have
• No age range/indication of ages applicable as I wish to help and treat everyone (above the age of 10 for I do not specialise in paediatric osteopathy)

```html
<!DOCTYPE html>
<html lang="en">
<head>
<meta charset="utf-8">
<title>Belvan Toske Osteopath Flyer</title>
<link href="https://fonts.googleapis.com/css2?family=Arimo:wght@400;700&family=Lato:wght@400;700&display=swap" rel="stylesheet">
<style>
  :root {
    --blue-deep: #1d5aa3;
    --blue-mid: #3277b5;
    --blue-bright: #2a72c0;
    --blue-sky: #34a7d7;
    --blue-soft: #85cae6;
    --white: #ffffff;
    --ink: #1e1e1e;
    --stage: #d4d4d4;
  }
  * { box-sizing: border-box; margin: 0; padding: 0; }
  html, body { width: 800px; height: 1200px; overflow: hidden; }
  body { background: var(--stage); position: relative; font-family: "Arimo", Arial, sans-serif; }

  .sheet { position: absolute; top: 325px; width: 388px; height: 550px; box-shadow: 0 6px 14px rgba(0,0,0,.25); overflow: hidden; background: var(--white); }
  .sheet--front { left: 8px; }
  .sheet--back { left: 404px; }
  .flyer { position: absolute; left: 0; top: 0; width: 695px; height: 985px; transform: scale(0.5583); transform-origin: 0 0; background: var(--white); overflow: hidden; }

  .hero-art { position: absolute; left: 0; top: 0; width: 695px; height: 540px; display: block; }
  .brand { position: absolute; display: flex; align-items: center; gap: 10px; font-family: "Arimo", Arial, sans-serif; font-weight: 400; line-height: 1.15; }
  .brand__mark { width: 16px; height: 16px; border-radius: 50%; }
  .brand__name { font-size: 21px; }
  .brand__role { font-size: 16px; }
  .brand--light { left: 62px; top: 62px; color: var(--white); }
  .brand--light .brand__mark { background: var(--white); }
  .brand--dark { left: 70px; top: 36px; color: var(--blue-mid); }
  .brand--dark .brand__mark { background: var(--blue-mid); }

  .headline { position: absolute; left: 18px; top: 270px; color: var(--white); font-family: "Arimo", Arial, sans-serif; font-weight: 700; line-height: 1; }
  .headline span { display: block; }
  .headline__l1 { font-size: 46px; }
  .headline__l2, .headline__l3 { font-size: 58px; }

  .intro { position: absolute; left: 32px; top: 548px; width: 635px; font-family: "Lato", Arial, sans-serif; font-size: 12.6px; line-height: 15.6px; color: var(--ink); }
  .intro p + p { margin-top: 13px; }

  .prices { position: absolute; left: 0; top: 780px; width: 695px; height: 93px; display: flex; }
  .price { flex: 1; display: flex; align-items: center; justify-content: center; text-align: center; color: var(--white); font-weight: 700; font-size: 20.5px; line-height: 25px; letter-spacing: .2px; }
  .price--intro { background: linear-gradient(90deg, #2d8bc8, var(--blue-sky)); }
  .price--follow { background: linear-gradient(90deg, var(--blue-deep), #1b4f8e); border-left: 2px solid var(--white); }
  .offer { position: absolute; left: 0; top: 873px; width: 695px; height: 44px; display: flex; align-items: center; justify-content: center; font-family: "Lato", Arial, sans-serif; font-size: 16px; color: #111; }
  .offer strong { margin-right: 4px; }
  .contact-bar { position: absolute; left: 0; top: 917px; width: 695px; height: 68px; background: linear-gradient(90deg, var(--blue-bright), #2a6fbd); display: flex; align-items: center; justify-content: space-around; padding: 0 28px; font-family: "Lato", Arial, sans-serif; font-size: 13px; color: var(--white); }
  .contact-bar__item { display: flex; align-items: center; gap: 8px; }
  .contact-bar svg { width: 15px; height: 15px; }

  .back-photo { position: absolute; left: 0; top: 0; width: 695px; height: 780px;
    background:
      radial-gradient(ellipse 120px 330px at 470px 470px, rgba(255,90,90,.22), rgba(255,90,90,0) 70%),
      radial-gradient(ellipse 300px 520px at 500px 480px, #a9a9a9, rgba(169,169,169,0) 75%),
      linear-gradient(90deg, #ffffff 28%, #e6e6e6 52%, #c4c4c4 100%); }
  .section-title { position: absolute; left: 32px; top: 106px; color: var(--blue-mid); font-weight: 700; font-size: 29px; letter-spacing: .3px; }
  .section-rule { position: absolute; left: 32px; top: 144px; width: 272px; height: 4px; background: var(--blue-sky); }
  .treatments { position: absolute; left: 40px; top: 153px; list-style: none; font-size: 14px; color: var(--ink); }
  .treatments li { height: 27.7px; display: flex; align-items: center; gap: 14px; }
  .treatments svg { width: 13px; height: 11px; }
  .clinic { position: absolute; left: 40px; top: 680px; display: flex; gap: 12px; color: var(--ink); font-size: 13.5px; line-height: 17px; }
  .clinic svg { width: 17px; height: 24px; margin-top: 32px; }
  .clinic address { font-style: normal; }
  .clinic__name { color: var(--blue-mid); font-weight: 700; font-size: 17px; line-height: 24px; }
</style>
</head>
<body>

<div class="sheet sheet--front">
  <div class="flyer">
    <svg class="hero-art" viewBox="0 0 695 540">
      <defs>
        <linearGradient id="frontPhoto" x1="0" y1="0" x2="1" y2="0">
          <stop offset="0" stop-color="#8c8c8c"/>
          <stop offset="0.55" stop-color="#b8b8b8"/>
          <stop offset="1" stop-color="#e0e0e0"/>
        </linearGradient>
        <radialGradient id="armTone" cx="0.6" cy="0.35" r="0.45">
          <stop offset="0" stop-color="#d8d8d8"/>
          <stop offset="1" stop-color="#d8d8d8" stop-opacity="0"/>
        </radialGradient>
        <radialGradient id="painGlow" cx="0.5" cy="0.5" r="0.5">
          <stop offset="0" stop-color="#ff6060" stop-opacity=".55"/>
          <stop offset="1" stop-color="#ff6060" stop-opacity="0"/>
        </radialGradient>
        <radialGradient id="blob" cx="0.6" cy="0.3" r="0.8">
          <stop offset="0" stop-color="#3d97d8"/>
          <stop offset="1" stop-color="#1c5fae"/>
        </radialGradient>
        <radialGradient id="insetWrist" cx="0.55" cy="0.5" r="0.6">
          <stop offset="0" stop-color="#f4c8c8"/>
          <stop offset="0.35" stop-color="#e8e8e8"/>
          <stop offset="1" stop-color="#9a9a9a"/>
        </radialGradient>
        <radialGradient id="insetShoulder" cx="0.5" cy="0.3" r="0.65">
          <stop offset="0" stop-color="#f2baba"/>
          <stop offset="0.35" stop-color="#e4e4e4"/>
          <stop offset="1" stop-color="#a0a0a0"/>
        </radialGradient>
      </defs>
      <rect x="0" y="0" width="695" height="540" fill="#ffffff"/>
      <g role="img" aria-label="Black and white photo of a man holding his sore elbow">
        <rect x="0" y="0" width="695" height="440" fill="url(#frontPhoto)"/>
        <rect x="280" y="0" width="415" height="330" fill="url(#armTone)"/>
        <circle cx="370" cy="175" r="60" fill="url(#painGlow)"/>
      </g>
      <path d="M0 420 C 180 600, 380 420, 520 330 C 590 285, 650 262, 695 255 L695 540 L0 540 Z" fill="var(--blue-deep)"/>
      <path d="M0 440 C 180 610, 390 450, 530 360 C 600 315, 655 295, 695 290 L695 540 L0 540 Z" fill="#ffffff"/>
      <path d="M0 200 C 120 150, 300 170, 345 290 C 380 390, 290 530, 110 528 C 60 527, 20 520, 0 512 Z" fill="url(#blob)"/>
      <circle cx="570" cy="400" r="88" fill="url(#insetShoulder)" stroke="var(--blue-sky)" stroke-width="6" role="img" aria-label="Photo of a hand resting on a sore shoulder"/>
      <circle cx="442" cy="402" r="88" fill="url(#insetWrist)" stroke="var(--blue-deep)" stroke-width="6" role="img" aria-label="Photo of a hand pressing a sore wrist"/>
    </svg>

    <div class="brand brand--light">
      <div>
        <div class="brand__name">Belvan Toske</div>
        <div class="brand__role">Osteopath &amp; Naturopath</div>
      </div>
      <span class="brand__mark"></span>
    </div>

    <h1 class="headline">
      <span class="headline__l1">BODYWISE</span>
      <span class="headline__l2">RESTFUL</span>
      <span class="headline__l3">HEALING</span>
    </h1>

    <div class="intro">
      <p>Osteopathy can offer great results for those seeking immediate care with painful conditions and also for those wishing to invest in long-term health solutions. Treatments are tailored to the individual’s need, regardless of age or condition, my goal is to provide the best medical care whether it be treatment or more appropriate referral.</p>
      <p>Osteopathy focuses on health promotion and disease prevention in order to help each person achieve a high level of wellness.</p>
      <p>Osteopathy uses conventional medical assessment and techniques when gathering detail during diagnostic procedures. However, the real strength of osteopathy lies within the unique approach to which a patient and the condition are assessed and treated. Each patient is assessed from both a mechanical and functional viewpoint and treatment is based on these findings and patient requirements. Manual treatment methods are applied to suit the needs of the individual patient.</p>
      <p>The overall goal is to achieve wellness by restoring balance and flexibility to the whole body.</p>
    </div>

    <div class="prices">
      <div class="price price--intro">INITIAL CONSULTATION £55<br>FOR 45 MINUTES</div>
      <div class="price price--follow">FOLLOW-UP TREATMENT<br>£50 FOR 30 MINUTES</div>
    </div>
    <div class="offer"><strong>20% OFF</strong> with this flyer (*for initial consultation only*)</div>
    <div class="contact-bar">
      <span class="contact-bar__item"><svg viewBox="0 0 16 16"><circle cx="8" cy="8" r="7" fill="none" stroke="#fff" stroke-width="1.3"/><path d="M5.5 4.5l1.5 1.5-1 1c.6 1.3 1.6 2.3 3 3l1-1 1.5 1.5-1.2 1.2C7.8 11.2 4.8 8.2 4.3 5.7Z" fill="#fff"/></svg>07461 352 417</span>
      <span class="contact-bar__item"><svg viewBox="0 0 16 16"><rect x="1" y="3.5" width="14" height="9" fill="#fff"/><path d="M1 3.5l7 5 7-5" fill="none" stroke="#2a72c0" stroke-width="1.2"/></svg>contact@belvantoske.co.uk</span>
      <span class="contact-bar__item"><svg viewBox="0 0 16 16"><g fill="none" stroke="#fff" stroke-width="1.2"><circle cx="8" cy="8" r="6.5"/><ellipse cx="8" cy="8" rx="3" ry="6.5"/><path d="M1.5 8h13M2.5 4.8h11M2.5 11.2h11"/></g></svg>www.belvantoske.co.uk</span>
    </div>
  </div>
</div>

<div class="sheet sheet--back">
  <div class="flyer">
    <div class="back-photo" role="img" aria-label="Black and white photo of a man from behind holding his neck and lower back, with red highlights along the spine"></div>

    <div class="brand brand--dark">
      <div>
        <div class="brand__name">Belvan Toske</div>
        <div class="brand__role">Osteopath &amp; Naturopath</div>
      </div>
      <span class="brand__mark"></span>
    </div>

    <h2 class="section-title">TREATMENT AREAS</h2>
    <div class="section-rule"></div>

    <ul class="treatments">
      <li><svg viewBox="0 0 13 11"><path d="M1 6l4 4 7-9" fill="none" stroke="#3277b5" stroke-width="2.2"/></svg>Headaches</li>
      <li><svg viewBox="0 0 13 11"><path d="M1 6l4 4 7-9" fill="none" stroke="#3277b5" stroke-width="2.2"/></svg>Neck pain</li>
      <li><svg viewBox="0 0 13 11"><path d="M1 6l4 4 7-9" fill="none" stroke="#3277b5" stroke-width="2.2"/></svg>Shoulder pain</li>
      <li><svg viewBox="0 0 13 11"><path d="M1 6l4 4 7-9" fill="none" stroke="#3277b5" stroke-width="2.2"/></svg>Elbow and hand pain</li>
      <li><svg viewBox="0 0 13 11"><path d="M1 6l4 4 7-9" fill="none" stroke="#3277b5" stroke-width="2.2"/></svg>Back pain</li>
      <li><svg viewBox="0 0 13 11"><path d="M1 6l4 4 7-9" fill="none" stroke="#3277b5" stroke-width="2.2"/></svg>Hip pain</li>
      <li><svg viewBox="0 0 13 11"><path d="M1 6l4 4 7-9" fill="none" stroke="#3277b5" stroke-width="2.2"/></svg>Knee pain</li>
      <li><svg viewBox="0 0 13 11"><path d="M1 6l4 4 7-9" fill="none" stroke="#3277b5" stroke-width="2.2"/></svg>Ankle and foot pain</li>
      <li><svg viewBox="0 0 13 11"><path d="M1 6l4 4 7-9" fill="none" stroke="#3277b5" stroke-width="2.2"/></svg>Arthritic pains</li>
      <li><svg viewBox="0 0 13 11"><path d="M1 6l4 4 7-9" fill="none" stroke="#3277b5" stroke-width="2.2"/></svg>Chronic pain</li>
      <li><svg viewBox="0 0 13 11"><path d="M1 6l4 4 7-9" fill="none" stroke="#3277b5" stroke-width="2.2"/></svg>Sciatica</li>
      <li><svg viewBox="0 0 13 11"><path d="M1 6l4 4 7-9" fill="none" stroke="#3277b5" stroke-width="2.2"/></svg>Arthritic Pain</li>
      <li><svg viewBox="0 0 13 11"><path d="M1 6l4 4 7-9" fill="none" stroke="#3277b5" stroke-width="2.2"/></svg>Joint Stiffness</li>
      <li><svg viewBox="0 0 13 11"><path d="M1 6l4 4 7-9" fill="none" stroke="#3277b5" stroke-width="2.2"/></svg>Sports Injuries</li>
      <li><svg viewBox="0 0 13 11"><path d="M1 6l4 4 7-9" fill="none" stroke="#3277b5" stroke-width="2.2"/></svg>Repetitive Strain</li>
      <li><svg viewBox="0 0 13 11"><path d="M1 6l4 4 7-9" fill="none" stroke="#3277b5" stroke-width="2.2"/></svg>Muscular Tension</li>
      <li><svg viewBox="0 0 13 11"><path d="M1 6l4 4 7-9" fill="none" stroke="#3277b5" stroke-width="2.2"/></svg>Work or Postural Strain</li>
      <li><svg viewBox="0 0 13 11"><path d="M1 6l4 4 7-9" fill="none" stroke="#3277b5" stroke-width="2.2"/></svg>Musculoskeletal Headaches</li>
      <li><svg viewBox="0 0 13 11"><path d="M1 6l4 4 7-9" fill="none" stroke="#3277b5" stroke-width="2.2"/></svg>Nutritional Advice or Alterations</li>
    </ul>

    <div class="clinic">
      <svg viewBox="0 0 17 24"><path d="M8.5 0C3.8 0 0 3.7 0 8.3 0 14 8.5 24 8.5 24S17 14 17 8.3C17 3.7 13.2 0 8.5 0Z" fill="#1d5aa3"/><circle cx="8.5" cy="8.3" r="3.2" fill="#fff"/></svg>
      <address>
        <div class="clinic__name">Copper Mead Clinic</div>
        La Rue Des Pins<br>St Lawrence, Jersey<br>JE2 4QW
      </address>
    </div>

    <div class="prices">
      <div class="price price--intro">INITIAL CONSULTATION £55<br>FOR 45 MINUTES</div>
      <div class="price price--follow">FOLLOW-UP TREATMENT<br>£50 FOR 30 MINUTES</div>
    </div>
    <div class="offer"><strong>20% OFF</strong> with this flyer (*for initial consultation only*)</div>
    <div class="contact-bar">
      <span class="contact-bar__item"><svg viewBox="0 0 16 16"><circle cx="8" cy="8" r="7" fill="none" stroke="#fff" stroke-width="1.3"/><path d="M5.5 4.5l1.5 1.5-1 1c.6 1.3 1.6 2.3 3 3l1-1 1.5 1.5-1.2 1.2C7.8 11.2 4.8 8.2 4.3 5.7Z" fill="#fff"/></svg>07461 352 417</span>
      <span class="contact-bar__item"><svg viewBox="0 0 16 16"><rect x="1" y="3.5" width="14" height="9" fill="#fff"/><path d="M1 3.5l7 5 7-5" fill="none" stroke="#2a72c0" stroke-width="1.2"/></svg>contact@belvantoske.co.uk</span>
      <span class="contact-bar__item"><svg viewBox="0 0 16 16"><g fill="none" stroke="#fff" stroke-width="1.2"><circle cx="8" cy="8" r="6.5"/><ellipse cx="8" cy="8" rx="3" ry="6.5"/><path d="M1.5 8h13M2.5 4.8h11M2.5 11.2h11"/></g></svg>www.belvantoske.co.uk</span>
    </div>
  </div>
</div>

</body>
</html>
```